L.M.T. Penrow

I am an indie author and already have a Facebook page. However, I would like it to be more professional and look less like a private Facebook page.

```html
<!DOCTYPE html>
<html lang="en">
<head>
<meta charset="utf-8">
<title>L.M.T. Penrow – Page Cover and Profile</title>
<link rel="stylesheet" href="https://fonts.googleapis.com/css2?family=Open+Sans:wght@300;400;700&display=swap">
<style>
  :root {
    --page-bg: #eef0f3;
    --brand-deep: #0b5f96;
    --brand-navy: #0b4f7f;
    --brand-sky: #19a4e2;
    --frame-line: #3a9fd4;
    --paper: #ffffff;
    --mist: #e3e5e7;
    --text-light: #ffffff;
  }
  * { margin: 0; padding: 0; box-sizing: border-box; }
  html, body {
    width: 1200px;
    height: 900px;
    overflow: hidden;
    background: var(--page-bg);
    font-family: "Open Sans", Arial, sans-serif;
  }
  .artboard {
    position: relative;
    width: 1200px;
    height: 900px;
  }
  .cover {
    position: absolute;
    left: 50px;
    top: 50px;
    width: 1100px;
    height: 417px;
    box-shadow: 0 6px 24px rgba(0,0,0,0.15);
  }
  .profile-tile {
    position: absolute;
    left: 50px;
    top: 510px;
    width: 340px;
    height: 340px;
    box-shadow: 0 6px 24px rgba(0,0,0,0.15);
  }
  svg { display: block; width: 100%; height: 100%; }
  .headline-light { font-family: "Open Sans", Arial, sans-serif; font-weight: 300; fill: var(--brand-navy); }
  .headline-bold { font-family: "Open Sans", Arial, sans-serif; font-weight: 700; fill: var(--brand-navy); }
  .author-name { font-family: "Open Sans", Arial, sans-serif; font-weight: 700; fill: var(--text-light); }
  .author-role { font-family: "Open Sans", Arial, sans-serif; font-weight: 400; fill: var(--text-light); }
</style>
</head>
<body>
<main class="artboard">

  <section class="cover" aria-label="Page cover">
    <svg viewBox="0 0 923 350" preserveAspectRatio="none">
      <defs>
        <linearGradient id="mistGradient" x1="0" y1="0" x2="1" y2="0">
          <stop offset="0" stop-color="#f4f4f4"/>
          <stop offset="0.6" stop-color="#ececec"/>
          <stop offset="1" stop-color="#d6d8da"/>
        </linearGradient>
        <linearGradient id="portraitTones" x1="0" y1="0" x2="1" y2="1">
          <stop offset="0" stop-color="#6f7a4c"/>
          <stop offset="0.4" stop-color="#c99a78"/>
          <stop offset="0.75" stop-color="#e2c3a4"/>
          <stop offset="1" stop-color="#c9cf8e"/>
        </linearGradient>
        <linearGradient id="bookTones" x1="0" y1="0" x2="0" y2="1">
          <stop offset="0" stop-color="#8a3a22"/>
          <stop offset="0.45" stop-color="#e0862c"/>
          <stop offset="1" stop-color="#1c1412"/>
        </linearGradient>
      </defs>

      <rect class="cover-base" x="0" y="0" width="923" height="350" fill="url(#mistGradient)"/>

      <!-- right blue field -->
      <polygon points="742,0 923,0 923,350 648,350" fill="var(--brand-deep)"/>
      <polygon points="728,0 742,0 648,350 634,350" fill="var(--paper)" opacity="0.9"/>
      <line x1="900" y1="0" x2="815" y2="320" stroke="#5fb4e4" stroke-width="1"/>
      <line x1="815" y1="320" x2="700" y2="320" stroke="#5fb4e4" stroke-width="1"/>
      <line x1="700" y1="320" x2="690" y2="350" stroke="#5fb4e4" stroke-width="1"/>

      <!-- left diagonal bands -->
      <polygon points="318,0 388,0 176,350 128,350" fill="var(--brand-sky)"/>
      <polygon points="340,0 388,0 176,350 150,350" fill="var(--brand-deep)"/>
      <polygon points="388,0 410,0 198,350 176,350" fill="var(--paper)"/>

      <!-- portrait area -->
      <polygon role="img" aria-label="Portrait photo of the author smiling outdoors" points="0,0 318,0 128,350 0,350" fill="url(#portraitTones)"/>

      <!-- author caption -->
      <text class="author-name" x="28" y="248" font-size="17">L.M.T. Penrow</text>
      <text class="author-role" x="28" y="259" font-size="10">Author of Suspense</text>
      <line x1="28" y1="265" x2="145" y2="265" stroke="var(--text-light)" stroke-width="0.7"/>
      <line x1="145" y1="265" x2="170" y2="225" stroke="var(--text-light)" stroke-width="0.7"/>

      <!-- headline frame -->
      <rect x="350" y="119" width="187" height="190" fill="none" stroke="var(--frame-line)" stroke-width="1"/>
      <polyline points="510,117 539,117 539,142" fill="none" stroke="var(--brand-navy)" stroke-width="3"/>
      <polyline points="348,285 348,311 376,311" fill="none" stroke="var(--brand-navy)" stroke-width="3"/>

      <text class="headline-light" x="362" y="166" font-size="42" textLength="165" lengthAdjust="spacingAndGlyphs">OPENING</text>
      <text class="headline-bold" x="362" y="200" font-size="37" textLength="165" lengthAdjust="spacingAndGlyphs">THE DOOR</text>
      <text class="headline-light" x="362" y="237" font-size="42" textLength="165" lengthAdjust="spacingAndGlyphs">TO ELENA</text>
      <text class="headline-bold" x="362" y="263" font-size="23" textLength="165" lengthAdjust="spacingAndGlyphs">WAS A FATAL</text>
      <text class="headline-light" x="362" y="298" font-size="40" textLength="167" lengthAdjust="spacingAndGlyphs">MISTAKE...</text>

      <!-- book editions -->
      <g role="img" aria-label="The novel shown as paperback, phone and tablet editions with fiery cover art">
        <rect x="576" y="85" width="110" height="178" fill="url(#bookTones)"/>
        <rect x="576" y="85" width="6" height="178" fill="#000" opacity="0.35"/>
        <rect x="714" y="107" width="99" height="146" rx="7" fill="#1b1b1b"/>
        <rect x="721" y="115" width="85" height="127" fill="url(#bookTones)"/>
        <rect x="667" y="140" width="58" height="118" rx="7" fill="#1b1b1b"/>
        <rect x="671" y="150" width="50" height="97" fill="url(#bookTones)"/>
      </g>
    </svg>
  </section>

  <section class="profile-tile" aria-label="Profile picture">
    <svg viewBox="0 0 200 200">
      <defs>
        <linearGradient id="profilePortrait" x1="0" y1="0" x2="1" y2="1">
          <stop offset="0" stop-color="#6f7a4c"/>
          <stop offset="0.5" stop-color="#d2a686"/>
          <stop offset="1" stop-color="#b8be80"/>
        </linearGradient>
      </defs>
      <rect x="0" y="0" width="200" height="200" fill="var(--brand-deep)"/>
      <polygon points="40,0 160,0 128,52 72,52" fill="var(--paper)"/>
      <polygon points="60,0 140,0 118,40 82,40" fill="var(--mist)"/>
      <circle cx="100" cy="104" r="66" fill="var(--paper)"/>
      <circle cx="100" cy="104" r="60" fill="#c9ccd0"/>
      <circle role="img" aria-label="Portrait photo of the author" cx="100" cy="104" r="56" fill="url(#profilePortrait)"/>
      <text class="author-name" x="100" y="139" font-size="9" text-anchor="middle">L.M.T. Penrow</text>
      <text class="author-role" x="100" y="147" font-size="5" text-anchor="middle">Author of Suspense</text>
    </svg>
  </section>

</main>
</body>
</html>
```